Health & Nutrition - Business Cards

Needs to look new-age, simple, and elegant. The cards are for my services/counsel in health and nutrition - which include mind, body, and soul. I would like to see something clean and simple but beautiful. Can have a plain background or with a pattern but I don't want it to take away from my contact details. Therefore, my info can be on the back of the card and a nice front design. I really like the flower of life symbol. The name of my business is called Willow Lantern.

Target Market(s)

Clients - men & women age 20-60. Adults, parents, teachers, sick individuals seeking nutrient counseling and dietary management.

Industry/Entity Type

Nutritionist

Contact Information for Business Card

Tomas Brindle
Cell: 345-582-7046
Email: tbrindle@mailvane.net

Colors
33a6d7
33b8a4
add136
ffffff
5c5c5c
f04a50
fbee3f
cedeed
85cae6

Requirements
Nice to have
• Maybe it can have some sort of sacred geometry as well, but not required. Nice to have the colors that I choose in the project but feel free to come up with your own use of colors. Thanks! =)

```html
<!DOCTYPE html>
<html lang="en">
<head>
<meta charset="utf-8">
<title>Willow Lantern – Business Cards</title>
<link rel="stylesheet" href="https://fonts.googleapis.com/css2?family=Raleway:wght@500&family=Lato:wght@400&display=swap">
<style>
  :root {
    --teal: #33b8a4;
    --charcoal: #5c5c5c;
    --white: #ffffff;
    --backdrop: #d9d9d9;
    --ink: #2a2a2a;
  }
  html, body {
    margin: 0;
    padding: 0;
    width: 1200px;
    height: 802px;
    overflow: hidden;
    background: var(--backdrop);
  }
  .canvas {
    position: relative;
    width: 1200px;
    height: 802px;
  }
  .card {
    position: absolute;
    top: 274px;
    width: 443px;
    height: 264px;
    overflow: hidden;
  }
  .card--front {
    left: 136px;
    background: var(--white);
  }
  .card--back {
    left: 624px;
    background: var(--teal);
  }
  .side-panel {
    position: absolute;
    left: 0;
    top: 0;
    width: 135px;
    height: 100%;
    background: var(--charcoal);
  }
  .brand-disc {
    position: absolute;
    left: 2px;
    top: 2px;
    width: 260px;
    height: 260px;
    border-radius: 50%;
    background: var(--teal);
  }
  .details {
    position: absolute;
    right: 22px;
    top: 0;
    height: 100%;
    text-align: right;
  }
  .business-name {
    position: absolute;
    right: 0;
    top: 42px;
    margin: 0;
    white-space: nowrap;
    font-family: "Raleway", sans-serif;
    font-weight: 500;
    font-size: 23px;
    line-height: 28px;
    color: var(--charcoal);
  }
  .business-name .accent,
  .person-name .accent { color: var(--teal); }
  .person-name {
    position: absolute;
    right: 0;
    top: 169px;
    margin: 0;
    white-space: nowrap;
    font-family: "Raleway", sans-serif;
    font-weight: 500;
    font-size: 19.5px;
    line-height: 24px;
    color: var(--charcoal);
  }
  .contact {
    position: absolute;
    right: 0;
    top: 205px;
    margin: 0;
    padding: 0;
    list-style: none;
    font-family: "Lato", sans-serif;
    font-size: 12.5px;
    line-height: 16px;
    color: var(--ink);
  }
  .contact li {
    display: flex;
    justify-content: flex-end;
    align-items: center;
    gap: 2px;
    white-space: nowrap;
  }
  .contact svg { width: 11px; height: 11px; fill: var(--teal); }
  .back-disc {
    position: absolute;
    left: 50%;
    top: 58px;
    width: 118px;
    height: 118px;
    margin-left: -59px;
    border-radius: 50%;
    background: var(--white);
  }
  .brand-name {
    position: absolute;
    left: 0;
    right: 0;
    top: 178px;
    margin: 0;
    text-align: center;
    font-family: "Raleway", sans-serif;
    font-weight: 500;
    font-size: 28px;
    line-height: 34px;
    color: var(--white);
  }
</style>
</head>
<body>
<main class="canvas">
  <section class="card card--front">
    <div class="side-panel"></div>
    <div class="brand-disc" aria-hidden="true"></div>
    <div class="details">
      <h1 class="business-name"><span class="accent">Willow</span> Lantern</h1>
      <h2 class="person-name"><span class="accent">Tomas</span> Brindle</h2>
      <ul class="contact">
        <li>345-582-7046
          <svg viewBox="0 0 12 12" aria-hidden="true"><path d="M1 4c0-1.5 2-2.5 5-2.5S11 2.5 11 4v1H8.5V3.8h-5V5H1zM3 6l1.5-1.5h3L9 6v4H3z"/></svg>
        </li>
        <li>tbrindle@mailvane.net
          <svg viewBox="0 0 12 12" aria-hidden="true"><path d="M1 2.5h10v7H1zM1.8 3.3v.5L6 6.8l4.2-3v-.5zM1.8 4.8v3.9l2.8-2zm8.4 0-2.8 1.9 2.8 2zM5.2 7.1 2.1 8.7h7.8L6.8 7.1 6 7.7z" fill-rule="evenodd"/></svg>
        </li>
      </ul>
    </div>
  </section>

  <section class="card card--back">
    <div class="back-disc" aria-hidden="true"></div>
    <p class="brand-name">Willow Lantern</p>
  </section>
</main>
</body>
</html>
```